Corvale Homes

To produce a business card design for our newly established house building and development company, We have had a logo design done please see attached, our slogan is "building your home sweet home"
Contact Information for Business Card
Adress on card needs to Read - 58 Elmsworth Lane, Kettering, Northamptonshire NN16 4QT. Director name Dean Vascotti
Requirements
Must have
- Web adress is www.corvale-homes.co.uk
- Email address is info@corvale-homes.co.uk
- phone number 07700 900417

```html
<!DOCTYPE html>
<html lang="en">
<head>
<meta charset="utf-8">
<title>Corvale Homes – Business Card</title>
<link rel="stylesheet" href="https://fonts.googleapis.com/css2?family=Open+Sans:ital,wght@0,400;0,600;0,700;1,600&display=swap">
<style>
  :root {
    --stage: #6c6d71;
    --card: #222223;
    --green: #8cc443;
    --white: #f2f2f2;
    --grey: #9a9a9c;
    --rule: #d9d9d9;
  }
  * { margin: 0; padding: 0; box-sizing: border-box; }
  html, body {
    width: 1200px; height: 1000px; overflow: hidden;
    background: var(--stage);
    font-family: "Open Sans", Arial, sans-serif;
  }
  .stage {
    position: relative; width: 1200px; height: 1000px;
    display: flex; align-items: center; justify-content: center; gap: 40px;
  }
  .card {
    position: relative; width: 540px; height: 320px;
    background: var(--card); border-radius: 26px;
    box-shadow: 0 14px 30px rgba(0,0,0,.35);
    overflow: hidden;
  }

  /* contact side */
  .contact .person { position: absolute; left: 40px; top: 44px; }
  .contact .person-name {
    color: var(--green); font-weight: 600; font-style: italic; font-size: 19px; line-height: 1.2;
  }
  .contact .person-role { color: var(--white); font-size: 14px; margin-top: 2px; }
  .contact .details {
    position: absolute; left: 40px; top: 118px;
    color: var(--white); font-size: 12.5px; line-height: 1.5; list-style: none;
  }
  .contact .divider {
    position: absolute; left: 210px; right: 40px; top: 162px;
    height: 1.5px; background: var(--rule);
  }
  .contact .brand {
    position: absolute; right: 40px; top: 52px;
    display: flex; align-items: center; gap: 10px;
  }
  .brand-mark { width: 22px; height: 22px; background: var(--green); }
  .brand-name { color: var(--green); font-weight: 700; font-size: 26px; line-height: 1; }
  .contact .address {
    position: absolute; right: 40px; bottom: 44px; text-align: right;
    color: var(--white); font-size: 12.5px; line-height: 1.5; font-style: normal;
  }

  /* brand side */
  .front { display: flex; flex-direction: column; align-items: center; justify-content: center; }
  .front .brand-name { font-size: 54px; letter-spacing: 1px; text-transform: uppercase; }
  .front .tagline-row {
    display: flex; align-items: center; gap: 12px; margin-top: 16px; width: 440px;
  }
  .front .tagline-rule { flex: 1; height: 1.5px; background: var(--grey); }
  .front .tagline {
    color: var(--green); font-size: 11px; letter-spacing: 3px; text-transform: uppercase; white-space: nowrap;
  }
</style>
</head>
<body>
  <main class="stage">
    <section class="card contact">
      <div class="person">
        <p class="person-name">Dean Vascotti</p>
        <p class="person-role">Director</p>
      </div>
      <ul class="details">
        <li>07700 900417</li>
        <li>www.corvale-homes.co.uk</li>
        <li>info@corvale-homes.co.uk</li>
      </ul>
      <div class="divider"></div>
      <div class="brand">
        <span class="brand-mark"></span>
        <span class="brand-name">Corvale Homes</span>
      </div>
      <address class="address">
        58 Elmsworth Lane, Kettering<br>
        Northamptonshire NN16 4QT
      </address>
    </section>

    <section class="card front">
      <span class="brand-name">Corvale Homes</span>
      <div class="tagline-row">
        <span class="tagline-rule"></span>
        <span class="tagline">Building your home sweet home</span>
        <span class="tagline-rule"></span>
      </div>
    </section>
  </main>
</body>
</html>
```